Vorlage für ein Workbook
Zielgruppe
Coaching und Beratung
Aufgabenstellung
Es soll eine Vorlage für ein Workbook erstellt werden, das ich dann selbst mit Inhalten füllen kann.. evtl. mit Canvas oder wie auch immer....
Es ist ein 12 Wochenkurs, d.h. ich brauche 1 Titelseite für jede Woche, die ich dann paste und copy machen kann und beschriften kann, sowie eine Vorlage für die einzelnen Seiten des Workbooks. Das Workbook in pdf Format muss auch online ausgefüllt werden können.
Design angepasst an Landingpage

```html
<!DOCTYPE html>
<html lang="de">
<head>
<meta charset="utf-8">
<title>Workbook – Titelseite</title>
<link rel="stylesheet" href="https://fonts.googleapis.com/css2?family=Cinzel+Decorative:wght@400&family=Cinzel:wght@400&display=swap">
<style>
  :root {
    --taupe: #c5bcb6;
    --sage: #b3bda5;
    --mist-blue: #c8d0d8;
    --blush: #f8ece8;
    --cream: #fbf6f2;
    --ink: #141212;
  }
  html, body {
    margin: 0;
    padding: 0;
    width: 849px;
    height: 1200px;
    overflow: hidden;
    background: var(--taupe);
  }
  .cover {
    position: relative;
    width: 849px;
    height: 1200px;
    overflow: hidden;
    background: var(--taupe);
  }
  .cover__shapes {
    position: absolute;
    inset: 0;
    width: 100%;
    height: 100%;
  }
  .shape--sage { fill: var(--sage); }
  .shape--blue { fill: var(--mist-blue); }
  .accent-line {
    fill: none;
    stroke: var(--cream);
    stroke-width: 2.2;
  }
  .branch-area { fill: url(#branch-glow); }
  .cover__title {
    position: absolute;
    left: 124px;
    top: 398px;
    margin: 0;
    font-family: "Cinzel Decorative", "Cinzel", serif;
    font-weight: 400;
    font-size: 63px;
    line-height: 1;
    color: var(--cream);
    white-space: nowrap;
  }
  .cover__subtitle {
    position: absolute;
    left: 136px;
    top: 482px;
    width: 520px;
    margin: 0;
    font-family: "Cinzel", serif;
    font-weight: 400;
    font-size: 28.5px;
    line-height: 34px;
    color: var(--ink);
    text-transform: uppercase;
  }
</style>
</head>
<body>
  <main class="cover">
    <svg class="cover__shapes" viewBox="0 0 793 1121" preserveAspectRatio="none">
      <defs>
        <radialGradient id="branch-glow" cx="0.55" cy="0.55" r="0.5">
          <stop offset="0" stop-color="#f8ece8" stop-opacity="0.55"/>
          <stop offset="0.6" stop-color="#f8ece8" stop-opacity="0.3"/>
          <stop offset="1" stop-color="#f8ece8" stop-opacity="0"/>
        </radialGradient>
      </defs>
      <rect class="shape--sage" x="0" y="0" width="2" height="757"/>
      <path class="shape--sage" d="M283 0 C285 80 300 130 370 150 C420 165 410 210 420 250 C440 320 520 340 610 355 C680 370 700 410 700 500 C700 570 740 600 793 605 L793 0 Z"/>
      <path class="accent-line" d="M280 0 C330 80 420 150 520 158 L640 160 C720 165 760 200 765 260 L770 400 C772 430 785 450 793 460"/>
      <path class="shape--blue" d="M0 757 C80 755 130 780 150 840 C170 920 190 1000 260 1060 C300 1090 350 1110 390 1121 L0 1121 Z"/>
      <ellipse class="branch-area" role="img" aria-label="Line illustration of a leafy branch with small berries"
               cx="610" cy="900" rx="260" ry="280"/>
    </svg>

    <h1 class="cover__title">Book Cover</h1>
    <p class="cover__subtitle">Please change this text with your own words</p>
  </main>
</body>
</html>
```